Hi Tobias, I need some designs for the front door and windows of our clinic, and some internal walls.

I have attached a picture of the front door and windows.
On them it needs
Sports Medicine
Pain Medicine
9371 6200
www.brindlemedgroup.com.au
Maybe the logo.

I will get it printed as stickers. Can you keep the blues, the font, and the Hexagon thing going.

I have also included 2 walls that I am thinking I would put a graphic on. One is behind the desk directly facing the front door/windows, the other is off to the right.

For the wall facing the door, maybe we have the Logo on it

For the other wall, maybe we put "Pain is a thief. Take back what's yours" in the cursive you have done before

See what you can magic up for me.

Cheers

Rob

```html
<!DOCTYPE html>
<html lang="en">
<head>
<meta charset="utf-8">
<title>Brindle Med Group – Window Decals</title>
<link rel="stylesheet" href="https://fonts.googleapis.com/css2?family=Teko:wght@500&family=Urbanist:wght@600&display=swap">
<style>
  :root {
    --bg: #f2efe9;
    --frame: #1e2226;
    --glass-light: #8fc3e0;
    --glass-mid: #4f95c2;
    --glass-deep: #2f6f9c;
    --handle: #b9bcbf;
    --text: #ffffff;
  }
  * { margin: 0; padding: 0; box-sizing: border-box; }
  html, body { width: 1200px; height: 565px; overflow: hidden; background: var(--bg); }
  .storefront { position: relative; width: 1200px; height: 565px; }
  .frame {
    position: absolute;
    top: 66px; left: 64px;
    width: 1050px; height: 484px;
    background: var(--frame);
  }
  .pane {
    position: absolute;
    background: linear-gradient(160deg, var(--glass-light) 0%, var(--glass-mid) 55%, var(--glass-deep) 100%);
    overflow: hidden;
  }
  .pane--left       { left: 86px;  top: 80px; width: 325px; height: 460px; }
  .pane--door-left  { left: 436px; top: 96px; width: 146px; height: 428px; }
  .pane--door-right { left: 614px; top: 96px; width: 142px; height: 428px; }
  .pane--right      { left: 784px; top: 80px; width: 310px; height: 460px; }
  .mullion { position: absolute; height: 9px; background: var(--frame); }
  .door-handle {
    position: absolute;
    top: 300px;
    width: 7px; height: 92px;
    border: 2px solid var(--handle);
    border-radius: 6px;
  }
  .panel-text {
    position: absolute;
    width: 325px;
    text-align: center;
    color: var(--text);
  }
  .service {
    font-family: "Teko", "Arial Narrow", sans-serif;
    font-weight: 500;
    font-size: 44px;
    line-height: 1;
    letter-spacing: 0.5px;
  }
  .phone {
    font-family: "Teko", "Arial Narrow", sans-serif;
    font-weight: 500;
    font-size: 46px;
    line-height: 1;
  }
  .web {
    font-family: "Urbanist", "Helvetica", sans-serif;
    font-weight: 600;
    font-size: 14px;
    letter-spacing: 0.8px;
    margin-top: -4px;
  }
</style>
</head>
<body>
  <main class="storefront">
    <div class="frame"></div>

    <div class="pane pane--left" role="img" aria-label="Blue glass decal with repeating hexagon outline pattern"></div>
    <div class="pane pane--door-left" role="img" aria-label="Blue door decal with repeating hexagon outline pattern"></div>
    <div class="pane pane--door-right" role="img" aria-label="Blue door decal with repeating hexagon outline pattern"></div>
    <div class="pane pane--right" role="img" aria-label="Blue glass decal with repeating hexagon outline pattern"></div>

    <div class="mullion" style="left:78px; top:190px; width:334px;"></div>
    <div class="mullion" style="left:78px; top:309px; width:334px;"></div>
    <div class="mullion" style="left:78px; top:426px; width:334px;"></div>
    <div class="mullion" style="left:780px; top:190px; width:322px;"></div>
    <div class="mullion" style="left:780px; top:307px; width:322px;"></div>
    <div class="mullion" style="left:780px; top:422px; width:322px;"></div>

    <div class="door-handle" style="left:581px;"></div>
    <div class="door-handle" style="left:606px;"></div>

    <section class="panel-text" style="left:86px; top:234px;">
      <h2 class="service">PAIN MEDICINE</h2>
    </section>
    <section class="panel-text" style="left:86px; top:346px;">
      <p class="phone">9371 6200</p>
      <p class="web">www.brindlemedgroup.com.au</p>
    </section>

    <section class="panel-text" style="left:776px; top:234px;">
      <h2 class="service">SPORTS MEDICINE</h2>
    </section>
    <section class="panel-text" style="left:776px; top:343px;">
      <p class="phone">9371 6200</p>
      <p class="web">www.brindlemedgroup.com.au</p>
    </section>
  </main>
</body>
</html>
```